Verpackungsdesign für Parfüm gesucht
Zielgruppe
Wir werden eine Marke unter dem Namen ORMAL mit Parfüm auf dem Markt bringen und benötigen hierfür ein hochwertiges Design . Unsre Zielgruppe ist m/w/d und zwischen 16 und 60 Jahre.
Aufgabenstellung
Bei der Verpackung handelt es sich um eine Schiebeschachtel. Wir benötigen das Design nur für die Außenhülle, nicht für den Schuber.
Pflichtangaben auf der Verpackung sind unser Logo, Eau de Parfum, High Intense, 20 ml e 0.67 FL OZ,
Natural Spray Vaporisateur,

```html
<!DOCTYPE html>
<html lang="de">
<head>
<meta charset="utf-8">
<title>ORMAL – Eau de Parfum High Intense, Faltschachtel</title>
<link rel="stylesheet" href="https://fonts.googleapis.com/css2?family=Open+Sans:wght@300;400&display=swap">
<style>
  :root {
    --paper: #ffffff;
    --ink-light: #a7a9ac;
    --mark-light: #c8c9cb;
    --band-light: #d1d2d4;
    --fold-light: #bcbec0;
    --board-dark: #3a3a3c;
    --ink-dark: #e6e7e8;
    --mark-dark: #d1d2d4;
    --band-dark: #a7a8ab;
    --band-dark-thin: #b8b9bb;
    --fold-dark: #5a5b5d;
  }
  * { margin: 0; padding: 0; box-sizing: border-box; }
  html, body { width: 1081px; height: 1200px; overflow: hidden; background: var(--paper); }
  body { font-family: "Open Sans", Arial, sans-serif; font-weight: 300; }

  .artboard {
    position: relative;
    width: 1150px;
    height: 1277px;
    transform: scale(0.9397);
    transform-origin: 0 0;
  }

  /* sleeve dieline */
  .sleeve {
    position: absolute;
    left: 55px;
    width: 1033px;
    height: 553px;
    --board: var(--paper);
    --ink: var(--ink-light);
    --mark: var(--mark-light);
    --band: var(--band-light);
    --band-thin: var(--band-light);
    --fold: var(--fold-light);
  }
  .sleeve--light { top: 52px; }
  .sleeve--dark {
    top: 667px;
    --board: var(--board-dark);
    --ink: var(--ink-dark);
    --mark: var(--mark-dark);
    --band: var(--band-dark);
    --band-thin: var(--band-dark-thin);
    --fold: var(--fold-dark);
  }

  .glue-flap { position: absolute; left: 0; top: 0; width: 117px; height: 553px; }

  .body-panel {
    position: absolute;
    left: 117px; top: 0;
    width: 916px; height: 553px;
    background: var(--board);
  }
  .band { position: absolute; left: 0; width: 100%; }
  .band--top { top: 0; height: 10px; background: var(--band); }
  .band--lower { top: 491px; height: 9px; background: var(--band-thin); }
  .band--base { top: 516px; height: 37px; background: var(--band); }

  .fold { position: absolute; top: 0; width: 1px; height: 100%; background: var(--fold); }
  .fold--a { left: 94px; }
  .fold--b { left: 459px; }
  .fold--c { left: 552px; }

  /* front face */
  .front { position: absolute; left: 94px; width: 365px; top: 0; height: 100%; color: var(--ink); text-align: center; }
  .brand-name {
    font-weight: 300;
    color: var(--mark);
    letter-spacing: 6px;
    line-height: 1;
  }
  .front .brand-name { position: absolute; top: 78px; width: 100%; font-size: 74px; }
  .product-type { position: absolute; top: 360px; width: 100%; font-size: 20px; letter-spacing: 1.5px; line-height: 1; }
  .product-name { position: absolute; top: 388px; width: 100%; font-size: 28px; font-weight: 400; line-height: 1; }
  .front .rule { position: absolute; top: 430px; left: 58px; width: 245px; height: 1px; background: var(--ink); }
  .spec-line {
    position: absolute; top: 442px; left: 58px; width: 245px;
    display: flex; justify-content: center; align-items: center;
    font-size: 12px; line-height: 18px; white-space: nowrap;
  }
  .spec-line .volume { border-left: 1px solid var(--ink); margin-left: 6px; padding-left: 6px; }

  /* back face */
  .back { position: absolute; left: 552px; width: 364px; top: 0; height: 100%; color: var(--ink); text-align: center; }
  .origin { position: absolute; top: 254px; width: 100%; font-size: 12.5px; line-height: 1; }
  .back .brand-name { position: absolute; top: 289px; width: 100%; font-size: 48px; letter-spacing: 4px; }
  .back .rule { position: absolute; top: 347px; left: 108px; width: 153px; height: 1px; background: var(--ink); }
  .address { position: absolute; top: 364px; width: 100%; font-size: 12.5px; line-height: 19px; font-style: normal; }
</style>
</head>
<body>
<main class="artboard">

  <section class="sleeve sleeve--light" aria-label="Hülle, helle Variante">
    <svg class="glue-flap" viewBox="0 0 117 553" aria-hidden="true">
      <polygon points="117,0 0,26 0,526 117,553" fill="#ffffff" stroke="#bcbec0" stroke-width="1"/>
    </svg>
    <div class="body-panel">
      <div class="band band--top"></div>
      <div class="band band--lower"></div>
      <div class="band band--base"></div>
      <div class="fold fold--a"></div>
      <div class="fold fold--b"></div>
      <div class="fold fold--c"></div>
      <div class="front">
        <p class="brand-name">ORMAL</p>
        <p class="product-type">EAU DE PARFUM</p>
        <p class="product-name">HIGH INTENSE</p>
        <div class="rule"></div>
        <p class="spec-line"><span>NATURAL SPRAY VAPORISATEUR</span><span class="volume">&#8494; 20 ml</span></p>
      </div>
      <div class="back">
        <p class="origin">Made in Germany</p>
        <p class="brand-name">ORMAL</p>
        <div class="rule"></div>
        <address class="address">Duftweg 12<br>D-40210 Musterstadt<br>WWW.ORMAL.EXAMPLE</address>
      </div>
    </div>
  </section>

  <section class="sleeve sleeve--dark" aria-label="Hülle, dunkle Variante">
    <svg class="glue-flap" viewBox="0 0 117 553" aria-hidden="true">
      <polygon points="117,0 0,23 0,523 117,553" fill="#3a3a3c"/>
    </svg>
    <div class="body-panel">
      <div class="band band--top"></div>
      <div class="band band--lower"></div>
      <div class="band band--base"></div>
      <div class="fold fold--a"></div>
      <div class="fold fold--b"></div>
      <div class="fold fold--c"></div>
      <div class="front">
        <p class="brand-name">ORMAL</p>
        <p class="product-type">EAU DE PARFUM</p>
        <p class="product-name">HIGH INTENSE</p>
        <div class="rule"></div>
        <p class="spec-line"><span>NATURAL SPRAY VAPORISATEUR</span><span class="volume">&#8494; 20 ml</span></p>
      </div>
      <div class="back">
        <p class="origin">Made in Germany</p>
        <p class="brand-name">ORMAL</p>
        <div class="rule"></div>
        <address class="address">Duftweg 12<br>D-40210 Musterstadt<br>WWW.ORMAL.EXAMPLE</address>
      </div>
    </div>
  </section>

</main>
</body>
</html>
```